Hernia Mesh Lawsuit - Banner & Creatives

Looking for design of ad banners and email creative for my Hernia Mesh Lawsuit website. Call to action based email focused on conveying brand, messaging of "have you had surgery using a surgical mesh, possibly for a hernia or a C-section? You may be eligible to join a surgical mesh class action lawsuit " and "ACT NOW: Check Your Eligibility Now." Call to action of 'Get Your Free Evaluation' or 'Fast, Free, No Obligation Evaluation'. Can use any messaging and images from the current website https://www.vorlastaclaims.com/herniamesh/find-out-if-youre-eligible/ Please focus on imaging that matches the site. The final Ad Banners must be delivered in both JPG and PSD file formats. Ad Banners must follow OWC standards. The final Email creative must be done in repsonsive HTML as well as text for easy use and include Email Opt Out link etc. <br/>We need Ad Banners in the following sizes.<br/><br/>• 728x90 Leaderboard<br/>• 300x250 Inline Rectangle<br/>• 320x50 Mobile<br/>Target Market(s)<br/><br/>NATIONAL INJURY LAWSUIT - Have you or a loved one had surgery using a surgical mesh, possibly for a hernia or a C-section? You may be eligible to join a surgical mesh class action lawsuit if you had another surgery to remove the mesh or if you suffered any side effects, including: Bleeding Bowel obstruction Fluid buildup (seromas) Infection Mesh migration Nerve damage Pain To qualify, the surgical mesh can be of any type, including Vela-Pro, B-LOXTM, Marvelle’s NuvaflexTM or any other brand.<br/>Industry/Entity Type<br/><br/>Lawyer<br/>Coding<br/><br/>Coded - Design and coding required<br/>Number of Pages Required<br/><br/>1 page<br/>Font styles to use<br/>Sans Serif<br/>Look and feel<br/><br/>Each slider illustrates characteristics of the customer's brand and the style your logo design should communicate.<br/>Elegant<br/>Bold<br/>Playful<br/>Serious<br/>Traditional<br/>Modern<br/>Personable<br/>Professional<br/>Feminine<br/>Masculine<br/>Colorful<br/>Conservative<br/>Economical<br/>Upmarket<br/><br/>Requirements<br/>Must have<br/><br/>* Call to action ad banners and Email creative.<br/>* Ad Banners in the 3 sizes noted in the project description.<br/>* Email creative must also be coded in responsive HTML.<br/>* The design must match the website https://varnell-benefitforms.com/<br/><br/>Nice to have<br/><br/>* Strong call to action<br/><br/>Should not have<br/><br/>* Should not be cookie cutter. Stick to simple yet official looking.

Target Market(s)

People who had another surgery to remove the mesh or if you suffered any side effects, including:

Bleeding
Bowel obstruction
Fluid buildup (seromas)
Infection

Mesh migration
Nerve damage
Pain

To qualify, the surgical mesh can be of any type, including Vela-Pro, B-LOXTM, Marvelle’s NuvaflexTM or any other brand.

Industry/Entity Type

Legal

Font styles to use
Serif

Colors

Designer to choose colors to be used in the design.

Requirements
Must have
• Must have
• * Call to action ad banners and Email creative.
• * Ad Banners in the 3 sizes noted in the project description.
• * Email creative must also be coded in responsive HTML.
• * The design must match the website https://varnell-benefitforms.com/
Nice to have
• Nice to have
• * Strong call to action
Should not have
• Should not have
• * Should not be cookie cutter. Stick to simple yet official looking.

```html
<!DOCTYPE html>
<html lang="en">
<head>
<meta charset="utf-8">
<title>Hernia Mesh Lawsuit – 300x250 Banner</title>
<link rel="stylesheet" href="https://fonts.googleapis.com/css2?family=Montserrat:wght@600;700;800&family=Lora:wght@400&display=swap">
<style>
  :root {
    --navy: #16246e;
    --blue: #2a4fb8;
    --violet: #6a3a9e;
    --magenta: #c8346e;
    --white: #ffffff;
    --sky: #55b8f2;
    --red: #e8212a;
  }
  * { margin: 0; padding: 0; box-sizing: border-box; }
  html, body { width: 1200px; height: 999px; overflow: hidden; background: var(--navy); }
  .banner {
    position: relative;
    width: 1200px;
    height: 999px;
    overflow: hidden;
    font-family: "Montserrat", Arial, sans-serif;
    color: var(--white);
  }
  .banner__backdrop {
    position: absolute;
    inset: 0;
    background:
      radial-gradient(ellipse 55% 60% at 88% 55%, rgba(214, 60, 120, 0.85), transparent 70%),
      radial-gradient(ellipse 45% 50% at 70% 20%, rgba(120, 90, 190, 0.55), transparent 70%),
      linear-gradient(100deg, var(--navy) 0%, var(--blue) 40%, var(--violet) 70%, var(--magenta) 100%);
  }
  .headline {
    position: absolute;
    left: 62px;
    top: 22px;
    font-weight: 800;
    line-height: 1;
    text-transform: uppercase;
  }
  .headline__lead { display: block; font-size: 75px; letter-spacing: 1px; }
  .headline__main { display: block; font-size: 108px; letter-spacing: 1px; margin-top: 22px; }
  .pitch {
    position: absolute;
    left: 68px;
    top: 282px;
    font-family: "Lora", Georgia, serif;
    font-size: 41px;
    line-height: 56px;
  }
  .pitch span { display: block; white-space: nowrap; }
  .urgency {
    position: absolute;
    left: 62px;
    top: 575px;
    font-size: 106px;
    font-weight: 800;
    color: var(--sky);
    line-height: 1;
    text-transform: uppercase;
  }
  .offer {
    position: absolute;
    left: 70px;
    top: 736px;
    font-size: 36px;
    font-weight: 600;
    letter-spacing: 3px;
    text-transform: uppercase;
  }
  .cta {
    position: absolute;
    left: 69px;
    top: 823px;
    width: 1076px;
    height: 142px;
    display: flex;
    background: var(--red);
    text-decoration: none;
    color: var(--white);
  }
  .cta__label {
    flex: 1;
    display: flex;
    align-items: center;
    padding-left: 85px;
    font-size: 50px;
    font-weight: 700;
    letter-spacing: 3px;
    text-transform: uppercase;
  }
  .cta__arrow {
    width: 176px;
    background: var(--white);
    display: flex;
    align-items: center;
    justify-content: center;
  }
</style>
</head>
<body>
  <div class="banner">
    <div class="banner__backdrop" role="img" aria-label="Close-up photo of a patient's side in a hospital gown, in deep blue and magenta tones"></div>

    <h1 class="headline">
      <span class="headline__lead">Injured from a hernia</span>
      <span class="headline__main">Mesh surgery?</span>
    </h1>

    <p class="pitch">
      <span>Have you had surgery using a surgical mesh,</span>
      <span>possibly for a hernia or a C-section? You may</span>
      <span>be eligible to join a surgical mesh class action</span>
      <span>lawsuit</span>
    </p>

    <p class="urgency">Act now</p>

    <p class="offer">Fast, free, no obligation evaluation</p>

    <a class="cta" href="#">
      <span class="cta__label">Free case evaluation</span>
      <span class="cta__arrow">
        <svg width="40" height="48" viewBox="0 0 40 48" aria-hidden="true">
          <polyline points="10,6 28,24 10,42" fill="none" stroke="#e8212a" stroke-width="9" stroke-linecap="square"/>
        </svg>
      </span>
    </a>
  </div>
</body>
</html>
```